Plastic Business Card for Bookkeeper

We are looking for a simple professional business card design to use for printing on thin frosted plastic (see-through) card stock. Logo and brand guideline documents are attached as well as a photo of our old business card, and another business card example that we like.

Target Market(s)

Small Business

Industry/Entity Type

Bookkeeper

Contact Information for Business Card

Harriet Olsen CPA
Chief Executive Bookkeeper
T. 03 5926 4417
M. 0438 761 205
E. harriet@pinecrestledger.com
W. www.pinecrestledger.com

Font styles to use
Sans Serif

Colors
6b449b
00a990

Requirements
Must have
• Stick with logo colors. Writing should be clear and easy to read and not too cramped together.
Nice to have
• Tag line for back of the card - 'Not your ordinary Bookkeeper'

```html
<!DOCTYPE html>
<html lang="en">
<head>
<meta charset="utf-8">
<title>Pinecrest Ledger – Business Card</title>
<link href="https://fonts.googleapis.com/css2?family=Roboto:ital,wght@0,400;0,500;0,700;1,500&display=swap" rel="stylesheet">
<style>
  :root {
    --backdrop: #2a2a2c;
    --frost-top: #c9cbcd;
    --frost-bottom: #a9abad;
    --frost-edge: rgba(255,255,255,0.55);
    --brand-purple: #6b449b;
    --brand-teal: #00a990;
    --contact-white: #ffffff;
    --muted-url: rgba(255,255,255,0.7);
  }
  * { margin: 0; padding: 0; box-sizing: border-box; }
  html, body {
    width: 1200px;
    height: 800px;
    overflow: hidden;
    background: var(--backdrop);
    font-family: "Roboto", Arial, sans-serif;
  }
  .canvas {
    width: 1200px;
    height: 800px;
    display: flex;
    align-items: center;
    justify-content: center;
  }
  .card {
    position: relative;
    width: 1000px;
    height: 572px;
    border-radius: 36px;
    background: linear-gradient(160deg, var(--frost-top), var(--frost-bottom));
    border: 2px solid var(--frost-edge);
    box-shadow: 0 24px 60px rgba(0,0,0,0.45);
  }
  .brand {
    position: absolute;
    left: 70px;
    top: 64px;
  }
  .brand-row {
    display: flex;
    align-items: center;
    gap: 18px;
  }
  .brand-dot {
    width: 54px;
    height: 54px;
    border-radius: 50%;
    background: var(--brand-teal);
  }
  .brand-name {
    font-weight: 500;
    font-size: 40px;
    letter-spacing: 1px;
    text-transform: uppercase;
    color: var(--brand-purple);
    line-height: 1;
  }
  .brand-url {
    margin: 10px 0 0 72px;
    font-size: 20px;
    color: var(--muted-url);
  }
  .contact {
    position: absolute;
    left: 70px;
    bottom: 70px;
    list-style: none;
    color: var(--contact-white);
    font-size: 24px;
    line-height: 1.45;
    text-shadow: 0 1px 2px rgba(0,0,0,0.25);
  }
  .person {
    position: absolute;
    right: 70px;
    bottom: 70px;
    text-align: right;
  }
  .person-name {
    font-weight: 700;
    font-size: 40px;
    color: var(--brand-teal);
    line-height: 1.1;
  }
  .person-title {
    font-weight: 500;
    font-style: italic;
    font-size: 26px;
    color: var(--brand-purple);
    margin-top: 4px;
  }
</style>
</head>
<body>
  <main class="canvas">
    <section class="card">
      <header class="brand">
        <div class="brand-row">
          <span class="brand-dot"></span>
          <span class="brand-name">Pinecrest Ledger</span>
        </div>
        <p class="brand-url">pinecrestledger.com</p>
      </header>

      <ul class="contact">
        <li>Tel. 03 5926 4417</li>
        <li>Mob. 0438 761 205</li>
        <li>harriet@pinecrestledger.com</li>
        <li>www.pinecrestledger.com</li>
      </ul>

      <div class="person">
        <p class="person-name">Harriet Olsen CPA</p>
        <p class="person-title">Chief Executive Bookkeeper</p>
      </div>
    </section>
  </main>
</body>
</html>
```